Luminously Grounded Vitality

We want to design a business card that is modern and appealing for an innovative psychedelic telemedicine company that provides at-home ketamine-assisted therapy along with wellness, longevity, and anti-aging medicines. We want to use our deep purple and white plus other colors you can find on our website. We don't have any strict brand guidelines yet so feel free to get creative. We want a very professional, but technology first modern design that will instill trust, peace, calm, but also be attractive to investors in the healthcare and SaaS space.

```html
<!DOCTYPE html>
<html lang="en">
<head>
<meta charset="utf-8">
<title>Luminously Business Card</title>
<link href="https://fonts.googleapis.com/css2?family=Lato:wght@300;400;700;900&display=swap" rel="stylesheet">
<style>
  :root {
    --plum-deep: #2b1a42;
    --violet: #7d68b3;
    --orchid: #a4609f;
    --ink: #2a2530;
    --paper: #ffffff;
    --stage: #eeecf1;
  }
  * { margin: 0; padding: 0; box-sizing: border-box; }
  html, body { width: 1200px; height: 977px; overflow: hidden; }
  body {
    background: var(--stage);
    font-family: "Lato", sans-serif;
    position: relative;
  }
  .card {
    position: absolute;
    left: 290px;
    width: 620px;
    height: 354px;
    border-radius: 22px;
    overflow: hidden;
    box-shadow: 0 10px 30px rgba(43, 26, 66, 0.18);
  }
  .card-front { top: 96px; background: var(--plum-deep); }
  .card-back { top: 510px; background: var(--paper); }

  /* Front */
  .front-brand {
    position: absolute;
    inset: 0;
    display: flex;
    flex-direction: column;
    align-items: center;
    justify-content: center;
    gap: 26px;
  }
  .front-mark {
    width: 54px; height: 54px;
    border-radius: 50%;
    background: var(--paper);
  }
  .front-wordmark {
    color: var(--paper);
    font-weight: 300;
    font-size: 58px;
    letter-spacing: 0.5px;
  }

  /* Back */
  .back-wave { position: absolute; left: 0; top: 0; width: 620px; height: 354px; }
  .back-wordmark {
    position: absolute;
    left: 78px; top: 40px;
    color: var(--orchid);
    font-weight: 300;
    font-size: 50px;
    display: flex; align-items: center; gap: 14px;
  }
  .back-mark {
    width: 26px; height: 26px; border-radius: 50%;
    background: var(--violet);
  }
  .person {
    position: absolute;
    left: 78px; top: 132px;
  }
  .person-name {
    color: var(--violet);
    font-weight: 900;
    font-size: 29px;
    letter-spacing: 0.3px;
  }
  .person-title {
    color: var(--orchid);
    font-size: 17px;
    margin-top: 2px;
  }
  .divider {
    position: absolute;
    left: 330px; top: 122px;
    width: 1.5px; height: 92px;
    background: var(--violet);
  }
  .contact {
    position: absolute;
    left: 348px; top: 120px;
    list-style: none;
    color: var(--ink);
    font-size: 13px;
    line-height: 1.45;
  }
  .contact li { display: flex; gap: 8px; align-items: flex-start; margin-bottom: 4px; }
  .contact svg { width: 11px; height: 11px; margin-top: 3px; flex: none; fill: var(--violet); }
  .contact .phone { font-size: 15px; }
  .website {
    position: absolute;
    right: 32px; bottom: 26px;
    color: var(--paper);
    font-size: 13px;
    letter-spacing: 1px;
  }
</style>
</head>
<body>
  <section class="card card-front">
    <div class="front-brand">
      <div class="front-mark"></div>
      <div class="front-wordmark">Luminously</div>
    </div>
  </section>

  <section class="card card-back">
    <svg class="back-wave" viewBox="0 0 620 354" aria-hidden="true">
      <path d="M150 354 C330 346 400 256 490 240 C550 230 595 228 620 228 L620 354 Z" fill="#7d68b3"/>
      <path d="M170 354 C340 348 410 266 498 252 C556 243 596 242 620 242 L620 354 Z" fill="#ffffff"/>
      <path d="M180 354 C350 350 418 274 504 260 C560 251 598 250 620 250 L620 354 Z" fill="#2b1a42"/>
    </svg>

    <div class="back-wordmark"><span class="back-mark"></span>Luminously</div>

    <div class="person">
      <div class="person-name">DANIEL REYES</div>
      <div class="person-title">Founder &amp; CEO</div>
    </div>

    <div class="divider"></div>

    <ul class="contact">
      <li>
        <svg viewBox="0 0 12 12"><path d="M6 0a4 4 0 0 0-4 4c0 3 4 8 4 8s4-5 4-8a4 4 0 0 0-4-4zm0 5.5a1.5 1.5 0 1 1 0-3 1.5 1.5 0 0 1 0 3z"/></svg>
        <span>248 Aspen Row, Suite 900<br>Boulder, CO, US, 80301</span>
      </li>
      <li class="phone">
        <svg viewBox="0 0 12 12"><path d="M2.5 0.5l2 2.2-1 1.3c.7 1.6 2 2.9 3.5 3.5l1.3-1 2.2 2-1.2 2C5 11.8 0.2 7 0.5 1.7z"/></svg>
        <span>+1 555-014-2290</span>
      </li>
      <li>
        <svg viewBox="0 0 12 12"><path d="M0 2h12v8H0z M0 2l6 4.5L12 2" fill="none" stroke="#7d68b3" stroke-width="1.3"/></svg>
        <span>hello@luminously.com</span>
      </li>
    </ul>

    <div class="website">www.Luminously.com</div>
  </section>
</body>
</html>
```